Meridale Counsel Corp Business Card design and layout

Meridale Counsel is a small, professional advisory firm specializing in business process consulting and advisory services. We are focused in the energy sector. The business card is to have a combination of blue shades and be professional and serious in nature. Investment banking, capital management, and professional service company card layouts should be used for similar templates

Target Market(s)

Medium to major corporations.

Industry/Entity Type

Consulting

Contact Information for Business Card

The card is to be professional looking in nature and must incorporate the company logo and name in some manner. A two sided design where the opposite side has a QR code and the logo is required.

Logo Text

Brastonhill Partners Inc.

Colors
0592cd
0455a3
3276b5
33a6d7
85cae6
85abd2
cee9f5
cedeed
ecf7fb

Requirements
Must have
• The card is to be professional and have space for employee, title, address, website, and phone numbers (office and cell). The layout must be some shades of blue.
Nice to have
• A space for embossing and/or some subtle gold highlights
Should not have
• Rainbow colours, unprofessional looking fonts (scribble, cursive writing)

```html
<!DOCTYPE html>
<html lang="en">
<head>
<meta charset="utf-8">
<title>Meridale Counsel Corp — Business Card</title>
<link href="https://fonts.googleapis.com/css2?family=Open+Sans:wght@400;600&display=swap" rel="stylesheet">
<style>
  :root {
    --backdrop: #e4e4df;
    --card-blue: #1a6fbd;
    --card-white: #f7f7f5;
    --ink-blue: #0455a3;
    --name-blue: #3276b5;
    --text-dark: #1d1d1f;
    --icon-blue: #33a6d7;
    --gold: #c9a94e;
    --rule-blue: #0455a3;
    --qr-fill: #ecf7fb;
  }
  * { box-sizing: border-box; margin: 0; padding: 0; }
  html, body { width: 1200px; height: 1200px; overflow: hidden; }
  body {
    background: var(--backdrop);
    font-family: "Open Sans", Arial, sans-serif;
    position: relative;
  }
  .card {
    position: absolute;
    width: 560px;
    height: 320px;
    border-radius: 3px;
  }
  .card--front {
    left: 110px;
    top: 170px;
    background: var(--card-blue);
    display: flex;
    align-items: center;
    justify-content: center;
  }
  .brand-front {
    display: flex;
    align-items: center;
    gap: 12px;
    color: var(--gold);
    font-weight: 600;
    font-size: 30px;
    letter-spacing: 1px;
  }
  .brand-front .brand-mark {
    width: 22px; height: 22px;
    background: var(--gold);
  }
  .qr-area {
    position: absolute;
    right: 26px;
    bottom: 26px;
    width: 64px;
    height: 64px;
    background: var(--qr-fill);
    border: 2px solid var(--gold);
  }
  .card--back {
    left: 530px;
    top: 640px;
    background: var(--card-white);
  }
  .brand-back {
    position: absolute;
    top: 40px;
    right: 36px;
    display: flex;
    align-items: center;
    gap: 9px;
    color: var(--ink-blue);
    font-weight: 600;
    font-size: 19px;
  }
  .brand-back .brand-mark {
    width: 14px; height: 14px;
    background: var(--ink-blue);
  }
  .person { position: absolute; left: 36px; top: 86px; }
  .person__name { color: var(--name-blue); font-size: 21px; font-weight: 400; line-height: 1.3; }
  .person__title { color: var(--ink-blue); font-size: 13px; }
  .contacts {
    position: absolute;
    left: 36px;
    top: 148px;
    list-style: none;
    font-size: 12.5px;
    color: var(--text-dark);
  }
  .contacts li { display: flex; align-items: center; gap: 9px; height: 21px; }
  .contacts svg { width: 13px; height: 13px; flex: none; }
  .address {
    position: absolute;
    left: 36px; right: 36px;
    top: 246px;
    display: flex;
    justify-content: center;
    align-items: center;
    gap: 7px;
    font-size: 12.5px;
    color: var(--text-dark);
  }
  .address svg { width: 11px; height: 14px; }
  .rule {
    position: absolute;
    left: 36px; right: 36px;
    top: 276px;
    border-top: 1.5px solid var(--rule-blue);
  }
</style>
</head>
<body>

  <section class="card card--front" aria-label="Card front">
    <div class="brand-front">
      <span class="brand-mark"></span>
      <span class="brand-name">Meridale Counsel Corp</span>
    </div>
    <div class="qr-area" role="img" aria-label="QR code area"></div>
  </section>

  <section class="card card--back" aria-label="Card back">
    <div class="brand-back">
      <span class="brand-mark"></span>
      <span class="brand-name">Meridale Counsel Corp</span>
    </div>

    <div class="person">
      <p class="person__name">Daniel Lavergne, P.Eng</p>
      <p class="person__title">President</p>
    </div>

    <ul class="contacts">
      <li>
        <svg viewBox="0 0 16 16" aria-hidden="true"><path fill="var(--icon-blue)" d="M3 2l3 0 1 3-2 1.5c.8 1.8 2.2 3.2 4 4L10.5 8.5l3 1 0 3c-6 1-11.5-4.5-10.5-10.5z"/></svg>
        <span>555-014-2290</span>
      </li>
      <li>
        <svg viewBox="0 0 16 16" aria-hidden="true"><rect x="4.5" y="1.5" width="7" height="13" rx="1.2" fill="none" stroke="var(--icon-blue)" stroke-width="1.4"/></svg>
        <span>000 000 0000</span>
      </li>
      <li>
        <svg viewBox="0 0 16 16" aria-hidden="true"><rect x="1" y="3.5" width="14" height="9" fill="var(--icon-blue)"/><path d="M1 3.5l7 5 7-5" fill="none" stroke="#fff" stroke-width="1.2"/></svg>
        <span>dlavergne@meridalecounsel.com</span>
      </li>
      <li>
        <svg viewBox="0 0 16 16" aria-hidden="true"><g fill="none" stroke="var(--icon-blue)" stroke-width="1.1"><circle cx="8" cy="8" r="6.5"/><ellipse cx="8" cy="8" rx="2.8" ry="6.5"/><path d="M1.5 8h13M2.5 5h11M2.5 11h11"/></g></svg>
        <span>www.meridalecounsel.com</span>
      </li>
    </ul>

    <p class="address">
      <svg viewBox="0 0 12 16" aria-hidden="true"><path fill="var(--icon-blue)" d="M6 0C2.7 0 0 2.6 0 5.8 0 10 6 16 6 16s6-6 6-10.2C12 2.6 9.3 0 6 0zm0 8.2A2.4 2.4 0 1 1 6 3.4a2.4 2.4 0 0 1 0 4.8z"/></svg>
      <span>300, 418- 9th Ave, SW, Alderbrook, AB, T4K 2M6</span>
    </p>
    <div class="rule"></div>
  </section>

</body>
</html>
```